Explainer Video Landing Page

We will soon have an "explainer" video which will explain to people in a graphical way what it is we do and the solutions we provide. Our current landing page design, located at http://www.lanternvoicecentral.com has a lot of different elements that we like, but won't focus on the new video we have as the "hero". We will want this new landing page to really showcase the video. Some of the other design elements we need are :
1- A link to "Get a Quote Online", in some way. This is the "goal" of the landing page.
2- We'll want some content sections under the video
3- We'll want the lead gen form to be there as well.
As an example, have a look at what BrisklyFern did. http://www.brisklyfern.com/
We like their example, but find it a bit busy. Our design should be cleaner with more whitespace. They are doing a lot of good things on that page that we'll want to mimic, like adding testimonials and existing customer logos.
Thank you in advance for participating in our design project.
Target Market(s)
Small and Mid-size Businesses. This will be a B2B landing page, focused on the communications needs of business.
Look and feel
Each slider illustrates characteristics of the customer's brand and the style your logo design should communicate.

```html
<!DOCTYPE html>
<html lang="en">
<head>
<meta charset="utf-8">
<title>Norvale – Explainer Video Landing Page</title>
<link rel="stylesheet" href="https://fonts.googleapis.com/css2?family=Roboto+Condensed:wght@400;700&family=Roboto:wght@400;700&display=swap">
<style>
:root{
  --accent:#f4583b;
  --ink:#222;
  --text:#444;
  --band:#efefef;
  --frame:#8e8e8e;
  --footer:#1f1f1f;
  --footer-text:#8a8a8a;
  --footer-head:#d6d6d6;
  --white:#fff;
}
*{margin:0;padding:0;box-sizing:border-box}
html,body{width:698px;height:1200px;overflow:hidden;background:var(--white)}
body{position:relative;font-family:"Roboto Condensed",Arial,sans-serif;color:var(--ink)}
.abs{position:absolute}

/* header */
.site-header{left:0;top:0;width:698px;height:41px;background:var(--white);border-bottom:2px solid #d0d0d0;box-shadow:0 2px 3px rgba(0,0,0,.15)}
.brand{left:96px;top:20px;font-weight:700;font-size:13px;letter-spacing:2.5px;color:var(--ink)}
.nav{top:20px;height:20px;font-size:8.5px;line-height:20px;color:var(--ink);font-family:Roboto,Arial,sans-serif}
.nav-home{background:var(--accent);color:var(--white);padding:0 5px}

/* hero */
.hero-title{left:0;top:58px;width:698px;text-align:center;font-weight:700;font-size:15px;letter-spacing:.3px}
.monitor{left:168px;top:84px;width:365px;height:178px;background:#0e0e0e;border-radius:2px}
.monitor-screen{left:176px;top:90px;width:349px;height:168px;background:linear-gradient(90deg,#5a4e44 0%,#c9b9a0 35%,#f2e6c8 60%,#d9b27a 80%,#8a6a44 100%)}
.monitor-base{left:156px;top:258px;width:390px;height:20px;background:linear-gradient(#3a3a3a,#111);border-radius:2px;box-shadow:0 4px 6px rgba(0,0,0,.35)}
.play{left:0;top:0}
.section-heading{left:0;top:292px;width:698px;text-align:center;font-weight:700;font-size:11px;color:#333}
.intro{left:144px;top:313px;width:410px;text-align:center;font-family:Roboto,Arial,sans-serif;font-size:6.3px;line-height:10px;color:var(--text)}
.btn{background:var(--accent);color:var(--white);font-weight:700;text-align:center;border-radius:4px}
.quote-btn{left:301px;top:353px;width:107px;height:27px;line-height:27px;font-size:10.5px}

/* plans */
.plans-band{left:0;top:395px;width:698px;height:146px;background:var(--band)}
.plan{top:407px;width:124px;height:119px;border:3px solid var(--frame);background:var(--white);text-align:center}
.plan-intro{left:89px;text-align:left;padding:20px 0 0 17px;font-size:14px;line-height:19px;color:var(--ink)}
.plan-icon{display:block;margin:3px auto 0}
.plan-name{font-weight:700;font-size:10px;line-height:11px;margin-top:4px}
.plan-text{font-size:6.5px;line-height:12px;margin:6px 6px 0;color:var(--ink)}

/* showcase video */
.showcase{left:89px;top:557px;width:521px;height:205px;background:radial-gradient(ellipse at 55% 45%,#e9c3a4 0%,#c68e6c 45%,#7a4e3a 100%)}
.thumb-arrow{top:762px;height:79px;background:#3a3535}
.thumb{top:762px;height:79px}

/* testimonials */
.testimonials-band{left:0;top:857px;width:698px;height:183px;background:var(--band)}
.avatar{width:44px;height:44px;border-radius:50%;border:2px solid var(--white);background:radial-gradient(circle at 50% 40%,#cfcfcf,#6a6a6a)}
.author{top:889px;font-size:8px;font-weight:700}
.author span{color:var(--accent)}
.quote{top:924px;width:230px;text-align:center;font-size:8.6px;line-height:21px;text-transform:uppercase;color:var(--ink)}
.more-btn{left:306px;top:1006px;width:90px;height:18px;line-height:18px;font-size:10px;border-radius:2px}

/* footer */
.site-footer{left:0;top:1040px;width:698px;height:160px;background:var(--footer)}
.foot-col{top:1051px;width:115px;font-family:Roboto,Arial,sans-serif}
.foot-col h3{font-weight:400;font-size:7.5px;color:var(--footer-head);padding-bottom:4px;border-bottom:1px solid #3a3a3a;margin-bottom:5px}
.foot-col li{list-style:none;font-size:6.3px;line-height:13px;color:var(--footer-text)}
.social li{display:flex;align-items:center;gap:5px;line-height:16px}
.social i{display:inline-block;width:10px;height:10px;border-radius:50%;background:#6b6b6b}
.legal{left:0;top:1168px;width:648px;text-align:center;font-family:Roboto,Arial,sans-serif;font-size:6.3px;line-height:12px;color:#6f6f6f}
.foot-brand{left:504px;top:1176px;font-weight:700;font-size:13px;letter-spacing:2.5px;color:var(--white)}
</style>
</head>
<body>

<header class="site-header abs"></header>
<div class="brand abs">NORVALE</div>
<nav>
  <span class="nav nav-home abs" style="left:344px">Home</span>
  <span class="nav abs" style="left:385px">Plans &amp; Pricing</span>
  <span class="nav abs" style="left:451px">Features</span>
  <span class="nav abs" style="left:496px">Phones</span>
  <span class="nav abs" style="left:538px">Learn More</span>
  <span class="nav abs" style="left:592px">Blog</span>
</nav>

<h1 class="hero-title abs">EXPLAIN TO PEOPLE THAT WHAT WE PROVIDE</h1>
<div class="monitor abs"></div>
<div class="monitor-screen abs" role="img" aria-label="Explainer video still: businessman in suit checking his phone in a bright office"></div>
<div class="monitor-base abs"></div>
<svg class="play abs" width="698" height="300" viewBox="0 0 698 300" aria-hidden="true">
  <circle cx="362" cy="174" r="36" fill="#000"/>
  <path d="M352 155 L381 174 L352 193 Z" fill="#fff"/>
</svg>

<h2 class="section-heading abs">What do we do?</h2>
<p class="intro abs">Lorem Ipsum is simply dummy text of the printing and typesetting industry. Lorem Ipsum has been the industry's standard dummy text ever since the 1500s, when an unknown printer took a galley of type and scrambled it to make a type specimen book. It has survived not only five centuries, but also the leap into electronic typesetting, remaining essentially unchanged.</p>
<a class="btn quote-btn abs">GET A QUOTE ONLINE</a>

<section class="plans-band abs"></section>
<div class="plan plan-intro abs"><b style="font-weight:400">SIMPLE PLANS<br>TO FIT YOUR<br>BUSINESS</b></div>

<div class="plan abs" style="left:222px">
  <svg class="plan-icon" width="38" height="38" viewBox="0 0 38 38" aria-hidden="true"><circle cx="19" cy="19" r="17" fill="#fff" stroke="#111" stroke-width="1.5"/><path d="M17 8h4l-1 3 3 15-4 4-4-4 3-15z" fill="#111"/></svg>
  <div class="plan-name">THE<br>STANDARD</div>
  <p class="plan-text">LOREM IPSUM IS SIMPLY DUMMY TEXT OF THE PRINTING AND TYPESETTING INDUSTRY.</p>
</div>
<div class="plan abs" style="left:353px">
  <svg class="plan-icon" width="38" height="38" viewBox="0 0 38 38" aria-hidden="true"><circle cx="19" cy="19" r="17" fill="#fff" stroke="#111" stroke-width="1.5"/><path d="M17 8h4l-1 3 3 15-4 4-4-4 3-15z" fill="#111"/><path d="M16 15l6-2M15.5 19l7-2.5M15 23l7-2.5" stroke="#fff" stroke-width="1"/></svg>
  <div class="plan-name">THE<br>EXTREME</div>
  <p class="plan-text">LOREM IPSUM IS SIMPLY DUMMY TEXT OF THE PRINTING AND TYPESETTING INDUSTRY.</p>
</div>
<div class="plan abs" style="left:484px">
  <svg class="plan-icon" width="38" height="38" viewBox="0 0 38 38" aria-hidden="true"><circle cx="19" cy="19" r="17" fill="#fff" stroke="#111" stroke-width="1.5"/><path d="M8 13l9 4v4l-9 4zM30 13l-9 4v4l9 4z" fill="#111"/><rect x="16" y="16" width="6" height="6" rx="1.5" fill="#111"/></svg>
  <div class="plan-name">THE<br>ULTIMATE</div>
  <p class="plan-text">LOREM IPSUM IS SIMPLY DUMMY TEXT OF THE PRINTING AND TYPESETTING INDUSTRY.</p>
</div>

<div class="showcase abs" role="img" aria-label="Video still: close-up of a fingertip touching a screen"></div>
<svg class="abs" style="left:0;top:0" width="698" height="842" viewBox="0 0 698 842" aria-hidden="true">
  <circle cx="358" cy="658" r="57" fill="#000"/>
  <path d="M341 627 L389 658 L341 689 Z" fill="#fff"/>
</svg>
<div class="thumb-arrow abs" style="left:89px;width:68px"></div>
<div class="thumb abs" style="left:157px;width:131px;background:linear-gradient(#f2f2f2,#c9c9cf)" role="img" aria-label="Thumbnail: business team smiling in an office"></div>
<div class="thumb abs" style="left:288px;width:122px;background:linear-gradient(135deg,#d8b48a,#9a6a44)" role="img" aria-label="Thumbnail: table football game close-up"></div>
<div class="thumb abs" style="left:410px;width:132px;background:linear-gradient(#3f82c8,#a9cbe8)" role="img" aria-label="Thumbnail: glass office tower against blue sky"></div>
<div class="thumb-arrow abs" style="left:542px;width:68px"></div>
<svg class="abs" style="left:0;top:762px" width="698" height="79" viewBox="0 0 698 79" aria-hidden="true">
  <path d="M146 29 L134 40 L146 51" fill="none" stroke="#fff" stroke-width="6"/>
  <path d="M554 29 L566 40 L554 51" fill="none" stroke="#fff" stroke-width="6"/>
</svg>

<section class="testimonials-band abs"></section>
<div class="avatar abs" style="left:154px;top:873px" role="img" aria-label="Portrait of Marcus Reed"></div>
<div class="author abs" style="left:216px"><span>MARCUS REED</span>, CEO</div>
<p class="quote abs" style="left:101px">Lorem ipsum is simply dummy text of the printing and typesetting industry. Lorem ipsum has been the industry's standard dummy text ever since the 1500s,</p>
<div class="avatar abs" style="left:420px;top:873px" role="img" aria-label="Portrait of Lena Hart"></div>
<div class="author abs" style="left:485px"><span>LENA HART</span>, CEO</div>
<p class="quote abs" style="left:366px">Lorem ipsum is simply dummy text of the printing and typesetting industry. Lorem ipsum has been the industry's standard dummy text ever since the 1500s,</p>
<a class="btn more-btn abs">+ READ MORE</a>

<footer class="site-footer abs"></footer>
<div class="foot-col abs" style="left:107px">
  <h3>Features &amp; Benefits</h3>
  <ul><li>Included Features</li><li>Optional Features</li><li>Conferencing</li><li>Can I keep my Phone Number?</li><li>Norvale VoIP Phones</li><li>Money Back Guarantee</li></ul>
</div>
<div class="foot-col abs" style="left:239px">
  <h3>Resources</h3>
  <ul><li>What is Hosted PBX</li><li>Frequently Asked Questions</li><li>Testimonials</li><li>Bill Online</li><li>Dashboard</li></ul>
</div>
<div class="foot-col abs" style="left:372px">
  <h3>Norvale</h3>
  <ul><li>Contact Us</li><li>Media Resources</li><li>Our History</li><li>Jobs</li><li>Norvale Pulse</li><li>NorTalk, our Blog</li></ul>
</div>
<div class="foot-col social abs" style="left:503px">
  <h3>Social</h3>
  <ul><li><i></i>Friendwall</li><li><i></i>Chirpline</li><li><i></i>ClipStream</li><li><i></i>Searchly+</li><li><i></i>ProLinker</li></ul>
</div>
<p class="legal abs">Call 1.877.55.NORVA or email sales@norvale.com<br>Copyright © 2014 Norvale. All rights reserved. This site has a Privacy policy.</p>
<div class="foot-brand abs">NORVALE</div>

</body>
</html>
```